We are an integrated facilities management company.

We aggregate everything related to facilities maintenance. Repair-replacement of equipment and facility space materials from:
Asset gathering and tracking.
Vendor screening, contracting and management.
Service requirement development.
Work order processing and management.
Invoice reconciliation.
Vendor payment.
Reporting.
Capital equipment bids and project management.

Target Market(s)

Retail, hospitality, multi-family housing, long term healthcare.

Industry/Entity Type

Maintenance

Contact Information for Business Card

Professional and bold look. (see logo zip file)

Colors
3377b5
85abd2
cedeed

Requirements
Must have
• N/A
Nice to have
• N/A
Should not have
• N/A

```html
<!DOCTYPE html>
<html lang="en">
<head>
<meta charset="utf-8">
<title>Northgate Facility Services – Business Card</title>
<link rel="stylesheet" href="https://fonts.googleapis.com/css2?family=Arimo:wght@400;700&display=swap">
<style>
  :root {
    --page-bg: #1b1d20;
    --card-bg: #23272b;
    --card-edge: #2c3136;
    --brand-blue: #3377b5;
    --brand-sky: #85abd2;
    --brand-mist: #cedeed;
    --text-grey: #8a929a;
    --rule-grey: #4a5158;
  }
  * { box-sizing: border-box; margin: 0; padding: 0; }
  html, body { width: 1200px; height: 800px; overflow: hidden; }
  body {
    background: var(--page-bg);
    font-family: "Arimo", Arial, sans-serif;
    position: relative;
  }
  .card {
    position: absolute;
    width: 560px;
    height: 320px;
    background: var(--card-bg);
    border: 1px solid var(--card-edge);
    border-radius: 3px;
    box-shadow: 0 18px 40px rgba(0,0,0,.45);
    overflow: hidden;
  }
  .card--services { left: 90px; top: 60px; }
  .card--contact { left: 550px; top: 420px; }

  .brand {
    display: flex;
    align-items: center;
    gap: 12px;
  }
  .brand__square {
    width: 22px;
    height: 22px;
    background: var(--brand-blue);
    flex: none;
  }
  .brand__name {
    font-weight: 700;
    font-size: 22px;
    letter-spacing: .5px;
    color: var(--brand-sky);
    text-transform: uppercase;
    line-height: 1;
    white-space: nowrap;
  }

  .card--services .brand { position: absolute; left: 40px; top: 42px; }
  .service-list {
    position: absolute;
    left: 42px;
    top: 100px;
    list-style: none;
  }
  .service-list li {
    font-size: 13px;
    color: var(--text-grey);
    line-height: 21px;
    display: flex;
    align-items: center;
    gap: 10px;
  }
  .service-list svg { width: 11px; height: 11px; flex: none; }
  .web-address {
    position: absolute;
    right: 24px;
    top: 40px;
    writing-mode: vertical-rl;
    font-size: 11px;
    letter-spacing: 3px;
    color: var(--brand-sky);
    text-transform: uppercase;
  }

  .card--contact .brand { position: absolute; left: 40px; top: 72px; }
  .divider {
    position: absolute;
    left: 40px;
    right: 40px;
    top: 150px;
    height: 1px;
    background: var(--rule-grey);
  }
  .person { position: absolute; left: 40px; top: 176px; }
  .person__name {
    font-weight: 700;
    font-size: 18px;
    color: var(--text-grey);
    text-transform: uppercase;
  }
  .person__role {
    font-size: 13px;
    color: var(--brand-sky);
    text-transform: uppercase;
    margin-top: 3px;
  }
  .contact-list {
    position: absolute;
    left: 40px;
    bottom: 34px;
    list-style: none;
  }
  .contact-list li {
    display: flex;
    align-items: center;
    gap: 8px;
    font-size: 13px;
    color: var(--text-grey);
    line-height: 22px;
  }
  .contact-list svg { width: 14px; height: 14px; flex: none; }
  .address {
    position: absolute;
    right: 40px;
    top: 170px;
    text-align: right;
    font-size: 13px;
    line-height: 20px;
    color: var(--text-grey);
    text-transform: uppercase;
  }
</style>
</head>
<body>

<section class="card card--services">
  <div class="brand">
    <span class="brand__square"></span>
    <span class="brand__name">Northgate Facility Services</span>
  </div>
  <ul class="service-list">
    <li><svg viewBox="0 0 10 10"><path d="M5 0V10M0 5H10M1.5 1.5L8.5 8.5M8.5 1.5L1.5 8.5" stroke="#85abd2" stroke-width="1.2"/></svg>Asset gathering and tracking.</li>
    <li><svg viewBox="0 0 10 10"><path d="M5 0V10M0 5H10M1.5 1.5L8.5 8.5M8.5 1.5L1.5 8.5" stroke="#85abd2" stroke-width="1.2"/></svg>Vendor screening, contracting and management.</li>
    <li><svg viewBox="0 0 10 10"><path d="M5 0V10M0 5H10M1.5 1.5L8.5 8.5M8.5 1.5L1.5 8.5" stroke="#85abd2" stroke-width="1.2"/></svg>Service requirement development.</li>
    <li><svg viewBox="0 0 10 10"><path d="M5 0V10M0 5H10M1.5 1.5L8.5 8.5M8.5 1.5L1.5 8.5" stroke="#85abd2" stroke-width="1.2"/></svg>Work order processing and management.</li>
    <li><svg viewBox="0 0 10 10"><path d="M5 0V10M0 5H10M1.5 1.5L8.5 8.5M8.5 1.5L1.5 8.5" stroke="#85abd2" stroke-width="1.2"/></svg>Invoice reconciliation.</li>
    <li><svg viewBox="0 0 10 10"><path d="M5 0V10M0 5H10M1.5 1.5L8.5 8.5M8.5 1.5L1.5 8.5" stroke="#85abd2" stroke-width="1.2"/></svg>Vendor payment.</li>
    <li><svg viewBox="0 0 10 10"><path d="M5 0V10M0 5H10M1.5 1.5L8.5 8.5M8.5 1.5L1.5 8.5" stroke="#85abd2" stroke-width="1.2"/></svg>Reporting.</li>
    <li><svg viewBox="0 0 10 10"><path d="M5 0V10M0 5H10M1.5 1.5L8.5 8.5M8.5 1.5L1.5 8.5" stroke="#85abd2" stroke-width="1.2"/></svg>Capital equipment bids and project management.</li>
  </ul>
  <div class="web-address">www.northgatefs.com</div>
</section>

<section class="card card--contact">
  <div class="brand">
    <span class="brand__square"></span>
    <span class="brand__name">Northgate Facility Services</span>
  </div>
  <div class="divider"></div>
  <div class="person">
    <p class="person__name">Jordan Hale</p>
    <p class="person__role">Owner</p>
  </div>
  <p class="address">PO Box 480, Mesa Ridge Road<br>Arizona 85001</p>
  <ul class="contact-list">
    <li>
      <svg viewBox="0 0 14 14"><circle cx="7" cy="7" r="6.3" fill="none" stroke="#85abd2" stroke-width="1.2"/><path d="M4.6 3.8l1.2-.3.8 1.8-.8.6c.4.9 1 1.5 1.9 1.9l.6-.8 1.8.8-.3 1.2c-2.9.2-5.4-2.3-5.2-5.2z" fill="#85abd2"/></svg>
      480.613.2790
    </li>
    <li>
      <svg viewBox="0 0 14 14"><circle cx="7" cy="7" r="6.3" fill="none" stroke="#85abd2" stroke-width="1.2"/><rect x="3.6" y="4.8" width="6.8" height="4.6" fill="none" stroke="#85abd2" stroke-width="1"/><path d="M3.6 4.8L7 7.6 10.4 4.8" fill="none" stroke="#85abd2" stroke-width="1"/></svg>
      info@northgatefs.com
    </li>
  </ul>
</section>

</body>
</html>
```